依頼詳細
「あなたの会社の近くに、こんないい足場会社があるよ」ということを伝えるチラシ
良い足場会社とは
資材を潤沢に持っているのでいつでも資材切れを起こさない
頼めばすぐ来てくれる(見積もり、施工)
早く、正確な施工
安全・安心
です。それらを惹起させるチラシの作成をお願いします。

一般住宅から、高層ビル・特殊な現場も請け負い可能
「安全かつ作業効率のいい足場」を提供
などの文言が入るといいです

チラシ配布対象者
工務店の現場監督さん、購買担当者さんです。

弊社の特徴
右肩上がりで成長している会社
くさび式足場を使用
記載項目
「とび工事一式・足場材リース」
建設業許可番号
社名、電話、FAX、メールアドレス、HP
材工一式(材料も施工も自社で行う、という意味)
サイズ
A4
ページ数
片面
希望イメージ
シンプル 複雑
単色 カラフル
暗い 明るい
日常 高級
遊び心 厳粛
未来的 伝統的
女性的 男性的
希望する色
青系
納品ファイル
• イラストレーター形式 (.ai)
補足説明

お客様の目に留まりやすそうなデザインで、配色がきれいで気に入りましたにいりました。
また修正も素早く対応いただきありがとうございました。

素敵なチラシをご提案いただきありがとうございました。

```html
<!DOCTYPE html>
<html lang="ja">
<head>
<meta charset="utf-8">
<title>株式会社 青嶺工業 足場チラシ</title>
<link href="https://fonts.googleapis.com/css2?family=Noto+Sans+JP:wght@300;400;500;700;900&family=Noto+Serif+JP:wght@500;700&display=swap" rel="stylesheet">
<style>
  :root {
    --navy: #17223f;
    --navy-deep: #0f1830;
    --indigo: #26307a;
    --red: #d6222a;
    --gold: #f0ac1e;
    --white: #ffffff;
    --ink: #1d2233;
    --sky-top: #f4f5f7;
    --sky-mid: #c9ccd2;
    --city: #7b818c;
  }
  * { margin: 0; padding: 0; box-sizing: border-box; }
  html, body { width: 846px; height: 1200px; overflow: hidden; background: var(--white); }
  .flyer {
    position: relative; width: 846px; height: 1200px; overflow: hidden;
    font-family: "Noto Sans JP", sans-serif; color: var(--ink); background: var(--white);
  }
  .hero-photo {
    position: absolute; left: 0; top: 0; width: 846px; height: 660px;
    background: linear-gradient(180deg, var(--sky-top) 0%, #e2e4e8 35%, var(--sky-mid) 65%, var(--city) 100%);
  }
  .hero-photo::after {
    content: ""; position: absolute; left: 330px; top: 0; width: 516px; height: 660px;
    background: radial-gradient(ellipse at 60% 35%, rgba(150,120,100,.35), rgba(150,120,100,0) 65%);
  }
  .brand {
    position: absolute; left: 26px; top: 22px;
    display: flex; align-items: center; gap: 10px;
    font-family: "Noto Serif JP", serif; font-weight: 700; color: var(--navy);
  }
  .brand-mark { width: 34px; height: 34px; background: var(--navy); border-radius: 50%; }
  .brand-name { font-size: 22px; letter-spacing: .04em; }
  .brand-name small { font-size: 13px; margin-right: 6px; }

  .headline { position: absolute; left: 0; top: 0; color: var(--red); }
  .headline-lead {
    position: absolute; left: 150px; top: 262px; white-space: nowrap;
    font-size: 56px; font-weight: 700; letter-spacing: .02em;
    text-shadow: 0 0 6px rgba(255,255,255,.9);
  }
  .headline-main {
    position: absolute; left: 100px; top: 310px; white-space: nowrap;
    font-size: 230px; font-weight: 300; line-height: 1; letter-spacing: -.02em;
    text-shadow: 0 0 8px rgba(255,255,255,.8);
  }
  .headline-tail {
    position: absolute; left: 452px; top: 568px; white-space: nowrap;
    font-size: 42px; font-weight: 500; letter-spacing: .04em;
    text-shadow: 0 0 6px rgba(255,255,255,.9);
  }

  .promise {
    position: absolute; left: 0; top: 660px; width: 846px; height: 285px;
    background: var(--navy); color: var(--white);
  }
  .promise-copy { position: absolute; left: 34px; top: 22px; }
  .promise-line { font-size: 58px; font-weight: 700; line-height: 80px; letter-spacing: .02em; white-space: nowrap; }
  .promise-sub {
    position: absolute; left: 240px; top: 30px; font-size: 17px; line-height: 28px; font-weight: 500;
  }
  .services { position: absolute; left: 598px; top: 26px; width: 222px; }
  .badge {
    background: var(--gold); color: var(--white); text-align: center;
    border-radius: 10px; padding: 8px 0 6px;
  }
  .badge-title { font-size: 28px; font-weight: 900; line-height: 1.1; }
  .badge-note { font-size: 14px; font-weight: 700; }
  .service-list {
    margin-top: 14px; background: var(--white); color: var(--navy);
    font-size: 34px; font-weight: 900; line-height: 50px; text-align: center; padding: 6px 0;
  }

  .footer { position: absolute; left: 0; top: 945px; width: 846px; height: 255px; background: var(--white); }
  .company { position: absolute; left: 26px; top: 22px; }
  .company-name { font-size: 22px; font-weight: 700; color: var(--navy); }
  .company-name small { font-size: 14px; margin-right: 6px; }
  .company-detail { margin-top: 8px; font-size: 12px; line-height: 20px; color: var(--ink); }
  .contact { position: absolute; left: 450px; top: 18px; width: 396px; }
  .tel-bar {
    background: var(--indigo); color: var(--white); height: 56px;
    display: flex; align-items: center; padding-left: 18px;
    font-size: 40px; font-weight: 700; letter-spacing: .01em;
  }
  .web { margin-top: 14px; padding-left: 18px; font-size: 14px; line-height: 26px; color: var(--ink); }
  .web span { display: inline-block; width: 34px; font-weight: 700; color: var(--indigo); }
</style>
</head>
<body>
<div class="flyer">
  <div class="hero-photo" role="img" aria-label="ヘルメットをかぶった作業員の横顔と高層ビルが並ぶ街並みの写真"></div>

  <div class="brand">
    <span class="brand-mark"></span>
    <span class="brand-name"><small>株式会社</small>青嶺工業</span>
  </div>

  <h1 class="headline">
    <span class="headline-lead">すべての</span>
    <span class="headline-main">足場</span>
    <span class="headline-tail">請負います。</span>
  </h1>

  <section class="promise">
    <div class="promise-copy">
      <p class="promise-line">安全で</p>
      <p class="promise-line">作業効率のいい</p>
      <p class="promise-line">足場を提供します。</p>
      <p class="promise-sub">一般住宅から高層ビルまで<br>特殊な現場も請け負います。</p>
    </div>
    <div class="services">
      <div class="badge">
        <div class="badge-title">材工一式</div>
        <div class="badge-note">くさび式足場を使用</div>
      </div>
      <div class="service-list">
        <div>鳶工事一式</div>
        <div>足場材リース</div>
        <div>鉄骨工事</div>
      </div>
    </div>
  </section>

  <footer class="footer">
    <div class="company">
      <div class="company-name"><small>株式会社</small>青嶺工業</div>
      <div class="company-detail">
        本社 〒920-0000 石川県金沢市青嶺町1-56<br>
        資材置場 〒920-0001 石川県金沢市港町48-1<br>
        mail / info@aomine-kogyo.com<br>
        FAX / 076-555-0183<br>
        許可番号 とび・土工工事業 石川県知事許可 第000号
      </div>
    </div>
    <div class="contact">
      <div class="tel-bar">tel.076-555-0182</div>
      <div class="web">
        <div><span>HP</span>www.aomine-kogyo.com</div>
        <div><span>SNS</span>www.instagram.com/aominekogyo</div>
      </div>
    </div>
  </footer>
</div>
</body>
</html>
```